Internal Office Slogans / Motto / Vision Statements

Hi. We would like to put up some posters around the office with quotations such as -
-”Do what you do so well that they will want to see it again and bring their friends.”- Harlan Pruett
-Make your customers feel heard and understood. Make your customers feel respected and liked. Make your customers feel appreciated and helped. Understand that you can do none of these things unless you are sincere about them.
Gordon Felsk
- It’s a very predictable and satisfying phenomenon: whenever we get better, our customers do too.
Ray Tolbin
-Catch people in the act of performing extraordinary customer service. Treat them like heroes. Tell their stories, far and wide.
Neil Hartcombe

The purpose of the posters is to reiterate our culture and vision within the organisation. They should be clean, crisp and eye catching, not gaudy or bright. Professional, bold and strong.

The company website and logo is at http://www.norvanta.com.au
Print size will be A1

Thanks for participating & looking forward to seeing your great work.
Updates

Hi All. . 

So to reiterate we are looking for one background design to be used for multiple quotes...  The list of quotes are as follows: 

Support and or Sales Office

 

Make your customers feel heard and understood.Make your customers feel respected and liked. Make your customers feelappreciated and helped. Understand that you can do none of these things unlessyou are sincere about them.

Gordon Felsk

 

Nothing liberates our greatness like the desireto help, the desire to serve

Rosalind Pevrell

 

It’s a very predictable and satisfying phenomenon:whenever we get better, our customers do too.

Ray Tolbin

 

Success means we go to sleep at night knowingthat our talents and abilities were used in a way that served others.

Rosalind Pevrell.

 

The sole purpose of business is to create, serveand satisfy a customer, from beginning to end – and that’s everyone’s job.

Neil Hartcombe

 

We don’t celebrate closing a sale, we celebrateopening a relationship.

Eleanor Quisk

I will never make you a promise – unless I giveyou a plan and procedure to make that promise possible.

Lon Borstad

 

Customers feel we take them for granted; onlyshow interest when we want an order; lavish our time on prospects; communicatemainly by invoice; are fixated on big accounts; drop them like hot potatoesonce we have the order; don’t follow through on promises; and satisfy our ownbureaucracy rather than their needs. We can do better than that, much better.

Peter K Almsby.

 

 

General and public area

 

Catch people in the act of performingextraordinary customer service. Treat them like heroes. Tell their stories, farand wide.

Neil Hartcombe

 

 

We see our customers as invited guests to aparty, and we are the hosts. It’s our job every day to make every importantaspect of the customer experience a little bit better." Carl Dunmore - Founder andCEO of Veltrona

 

"If you do build a great experience,customers tell each other about that. Word of mouth is verypowerful."  Carl Dunmore

 

It's not a faithin technology. It's faith in people. Frank Toller

 

“Being the richest man in the cemetery doesn’tmatter to me … Going to bed at night saying we’ve done something wonderful…that’s what matters to me.” Frank Toller

 

The customer experience is the next competitivebattleground. Terry Mandevic, CIO, Quorra Computers

 

”Do what you do so well that they will want tosee it again and bring their friends.”- Harlan Pruett

In the world of internet customer service, it isimportant to remember your competitor is only a mouse click away. GlennPirsley (not sure who he is but like the quote).

The customer is why you go to work. If they goaway, you do, too. Simon Largotti (?)

 

MaybeSome for Sales or Build Team:

Quality is remembered long after the price is forgotten. Renzoli Family Slogan

```html
<!DOCTYPE html>
<html lang="en">
<head>
<meta charset="utf-8">
<title>Norvanta – Customer Quote Poster</title>
<link rel="stylesheet" href="https://fonts.googleapis.com/css2?family=Roboto:ital,wght@0,300;0,400;0,700;0,900;1,300&display=swap">
<style>
  :root {
    --header-black: #141414;
    --brand-red: #d4192b;
    --ink: #161616;
    --muted: #8d8d8d;
    --footer-grey: #8a8a8a;
    --frame: #d2d2d2;
    --paper-top: #ffffff;
    --paper-bottom: #e4e4e4;
    --badge-navy: #1f3a7a;
  }
  * { margin: 0; padding: 0; box-sizing: border-box; }
  html, body {
    width: 849px;
    height: 1200px;
    overflow: hidden;
  }
  body {
    font-family: "Roboto", Arial, sans-serif;
    background: linear-gradient(180deg, var(--paper-top) 0%, #f6f6f6 45%, var(--paper-bottom) 100%);
    position: relative;
  }
  .poster-header {
    position: absolute;
    top: 0; left: 0;
    width: 849px;
    height: 92px;
    background: var(--header-black);
  }
  .brand {
    position: absolute;
    left: 50px;
    top: 24px;
    display: flex;
    align-items: center;
    gap: 10px;
  }
  .brand-mark {
    width: 38px;
    height: 38px;
    background: var(--brand-red);
  }
  .brand-name {
    color: #ffffff;
    font-weight: 700;
    font-size: 38px;
    line-height: 1;
    letter-spacing: -1px;
  }
  .poster-frame {
    position: absolute;
    left: 35px;
    top: 92px;
    width: 786px;
    height: 1071px;
    border: 1px solid var(--frame);
    border-top: none;
    border-radius: 0 0 6px 6px;
  }
  .quote {
    position: absolute;
    left: 62px;
    top: 468px;
    width: 740px;
    font-size: 23.5px;
    line-height: 36px;
    color: var(--ink);
    text-transform: uppercase;
    white-space: nowrap;
  }
  .quote .line { display: block; }
  .quote .light { font-weight: 300; }
  .quote .strong { font-weight: 700; }
  .quote .red { color: var(--brand-red); }
  .quote-author {
    position: absolute;
    left: 62px;
    top: 646px;
    font-size: 20px;
    font-style: italic;
    font-weight: 300;
    color: var(--muted);
  }
  .origin-badge {
    position: absolute;
    left: 684px;
    top: 1037px;
    width: 137px;
    height: 126px;
    border: 1px solid var(--frame);
    border-right: none;
    border-bottom: none;
    border-radius: 6px 0 0 0;
    background: linear-gradient(180deg, rgba(255,255,255,0.5), rgba(230,230,230,0.6));
  }
  .origin-badge svg {
    position: absolute;
    left: 30px;
    top: 20px;
  }
  .site-url {
    position: absolute;
    left: 0;
    top: 1171px;
    width: 849px;
    text-align: center;
    font-size: 13px;
    color: var(--footer-grey);
  }
</style>
</head>
<body>
  <header class="poster-header">
    <div class="brand">
      <span class="brand-mark"></span>
      <span class="brand-name">Norvanta</span>
    </div>
  </header>

  <div class="poster-frame"></div>

  <p class="quote">
    <span class="line"><span class="light red">Make your customers </span><span class="strong">feel heard and understood.</span></span>
    <span class="line"><span class="light">Make your customers </span><span class="strong red">feel respected and liked.</span></span>
    <span class="line"><span class="light">Make your customers </span><span class="strong">feel appreciated and helped.</span></span>
    <span class="line"><span class="strong red">Understand that </span><span class="strong">you can do none of these things</span></span>
    <span class="line"><span class="strong">unless you are sincere about them.</span></span>
  </p>
  <p class="quote-author">Gordon Felsk</p>

  <div class="origin-badge">
    <svg width="78" height="78" viewBox="0 0 78 78" role="img" aria-label="Locally owned badge">
      <rect x="4" y="4" width="70" height="70" rx="8" fill="var(--badge-navy)" opacity="0.85"/>
    </svg>
  </div>

  <footer class="site-url">norvanta.com.au</footer>
</body>
</html>
```